Website concept design - need very creative and polished web page layouts

Need 3-4 web pages designed (graphic only). Client is an interior designer and has specific design requirements. Need a skilled graphic designer to help me create a concept for the new site.

The site is primarily meant to allow users to build and buy a new product, but should have a portfolio site feel. I have specific requirements so designer won't have to 'figure it out' on their own.

Making use of white space, text orientation, and object movement are essential to the success of this project.

Inspirational sites:

http://brisk.tamo.site/#en - creative and atypical
https://pembly.io/ - white space and movement; vertical menu links
https://738q.jp- modern into, object hover movement
https://www.polnaxo.com/case-copper-reed - white space, dimensional feel of objects floating on page; pop of color

Target Market(s)

Interior designers and individuals - both commercial and retail.

Industry/Entity Type

Interior Design

Number of Pages Required

4 page

Font styles to use
Serif
Sans Serif

Requirements
Must have
• Professional design, meet design requirements, professional and highly creative look. This cannot look like or resemble in any way a common or typical website. Making use of white space, text orientation, and object movement are essential to the success of this project.
• Colors for the project:
• COLOR TREATMENT - (Not Final)
• DARK PUTTY – 77% Black
• R 95
• G 96
• B 98
• LIGHT PUTTY – 50% Black
• R 129
• G 131
• B 134
• ** Other Levels of Putty can be used.
• BLUE GREEN - (May not be final)
• R 113
• G 202
• B 210
Should not have
• Cannot look like or resemble a typical website design.

```html
<!DOCTYPE html>
<html lang="en">
<head>
<meta charset="utf-8">
<title>Valde — Interior Products</title>
<link rel="stylesheet" href="https://fonts.googleapis.com/css2?family=Bodoni+Moda:wght@400;500&family=DM+Sans:wght@400;500&display=swap">
<style>
:root{
  --canvas:#f4f4f4;
  --page:#ffffff;
  --ink:#1d1b1c;
  --dark:#232021;
  --ghost:#3a3637;
  --putty-dark:#5f6062;
  --putty-light:#818386;
  --teal:#71cad2;
  --white:#ffffff;
}
*{margin:0;padding:0;box-sizing:border-box}
html,body{width:1200px;height:3468px;overflow:hidden}
body{background:var(--canvas);font-family:"DM Sans",Arial,sans-serif;color:var(--ink);position:relative}
.page{position:absolute;left:28px;top:23px;width:1144px;height:3400px;background:var(--page)}
.abs{position:absolute;z-index:2}
.photo{position:absolute;z-index:1}
.serif{font-family:"Bodoni Moda",Georgia,serif}
.link{font-size:13px;letter-spacing:.3px;border-bottom:1.5px solid currentColor;padding-bottom:4px;display:inline-flex;align-items:center;gap:8px}

/* hero */
.hero-accent{left:0;top:0;width:12px;height:710px;background:var(--teal)}
.brand{left:55px;top:56px;font-family:"Bodoni Moda",Georgia,serif;font-size:19px;letter-spacing:1px;color:var(--ink)}
.menu{left:222px;top:57px;font-size:13px;display:flex;align-items:center;gap:10px}
.hero-title{left:222px;top:205px;font-size:52px;line-height:63px;font-weight:500;color:var(--ink);white-space:nowrap}
.hero-sub{left:222px;top:424px;font-size:17px;white-space:nowrap}
.hero-link{left:222px;top:587px;color:var(--ink)}
.slider{left:502px;top:585px;width:140px;height:36px;display:flex}
.slider span{flex:1;display:flex;align-items:center;justify-content:center}
.slider .prev{border:1.5px solid var(--ink);background:var(--page)}
.slider .next{background:var(--dark)}
.scroll{left:40px;top:700px;transform:rotate(-90deg);transform-origin:left top;font-size:12px;white-space:nowrap}
.hero-photo{left:573px;top:0;width:571px;height:710px;background:linear-gradient(160deg,#e8e3dc 0%,#cfc3b2 45%,#8c7a66 80%,#5c4c3e 100%)}
.topbar{left:837px;top:0;width:307px;height:127px;background:var(--dark);display:flex;align-items:center;justify-content:space-around;padding:0 30px;color:var(--white);font-size:13px}
.topbar .login{color:var(--teal);display:flex;align-items:center;gap:6px}

/* products */
.product-caption{font-size:21px;line-height:26px;font-weight:500;white-space:nowrap}
.tag{width:28px;background:var(--page);display:flex;align-items:center;justify-content:center}
.tag span{transform:rotate(-90deg);white-space:nowrap;font-size:10px;color:var(--putty-light)}
.view-all{left:166px;top:1842px;color:var(--teal)}

/* feature */
.feature-photo{left:0;top:1954px;width:1144px;height:615px;background:linear-gradient(100deg,#d9d3c8 0%,#c8b8a0 35%,#a4927a 60%,#6d6a50 80%,#e0ddd6 100%)}
.dark-tab{left:0;top:2393px;width:307px;height:176px;background:var(--dark)}
.dark-block{left:0;top:2569px;width:571px;height:390px;background:var(--dark)}
.feature-title{left:83px;top:2328px;font-size:48px;line-height:58px;color:var(--white);font-weight:400;white-space:nowrap}
.watch{left:83px;top:2500px;font-size:13px;color:var(--teal);display:flex;align-items:center;gap:8px}
.ghost{left:83px;top:2640px;font-size:58px;color:var(--ghost);letter-spacing:2px}
.dark-copy{left:166px;top:2676px;width:340px;font-size:19px;line-height:27px;color:var(--white)}
.side-copy{left:668px;top:2660px;width:400px;font-size:13px;line-height:23px;color:var(--putty-light)}
.side-copy p+p{margin-top:23px}
.explore{left:668px;top:2888px;color:var(--ink)}

/* newsletter */
.newsletter{left:83px;top:3047px;width:978px;height:176px;background:var(--teal)}
.news-copy{left:166px;top:3106px;font-size:20px;line-height:26px;color:var(--white)}
.news-input{left:668px;top:3132px;width:225px;border-bottom:1.5px solid var(--white);padding-bottom:10px;font-size:12px;color:var(--white)}
.news-submit{left:893px;top:3118px;width:86px;height:40px;background:var(--white);color:var(--teal);font-size:12px;display:flex;align-items:center;justify-content:center}

/* footer */
.foot-nav{left:83px;top:3293px;font-size:11px;letter-spacing:.3px;font-weight:500}
.foot-nav a{color:var(--ink);text-decoration:none;position:absolute;white-space:nowrap}
.foot-nav a.active{color:var(--teal)}
.social{left:924px;top:3290px;display:flex;gap:18px}
.social i{display:block;width:14px;height:14px;border-radius:50%;background:var(--ink)}
.copyright{left:83px;top:3338px;font-size:11px;color:var(--putty-light)}
.call{right:83px;top:3338px;font-size:11px;color:var(--putty-light)}
.call b{font-weight:400;color:var(--teal);margin-right:8px}
</style>
</head>
<body>
<main class="page">

  <!-- hero -->
  <div class="photo hero-photo" role="img" aria-label="Dining nook with pendant lamps, round wooden table and sculpted chair"></div>
  <div class="abs hero-accent"></div>
  <div class="abs brand">VALDE</div>
  <div class="abs menu">
    <svg width="16" height="12" viewBox="0 0 16 12"><path d="M0 1h16M0 6h16M0 11h16" stroke="#71cad2" stroke-width="1.6"/></svg>
    Menu
  </div>
  <h1 class="abs hero-title serif">Visualize<br>&nbsp;Your Room Into<br>&nbsp;A Masterpiece!</h1>
  <p class="abs hero-sub">Great Product Quality with Outstanding Design</p>
  <a class="abs link hero-link">Discover More <svg width="12" height="8" viewBox="0 0 12 8"><path d="M0 4h11M8 1l3 3-3 3" stroke="#1d1b1c" fill="none" stroke-width="1.3"/></svg></a>
  <div class="abs slider">
    <span class="prev"><svg width="14" height="8" viewBox="0 0 14 8"><path d="M14 4H1M4 1L1 4l3 3" stroke="#1d1b1c" fill="none" stroke-width="1.5"/></svg></span>
    <span class="next"><svg width="14" height="8" viewBox="0 0 14 8"><path d="M0 4h13M10 1l3 3-3 3" stroke="#fff" fill="none" stroke-width="1.5"/></svg></span>
  </div>
  <div class="abs scroll">← Scroll</div>
  <div class="abs topbar">
    <svg width="12" height="12" viewBox="0 0 12 12"><circle cx="5" cy="5" r="3.5" stroke="#fff" fill="none" stroke-width="1.5"/><path d="M7.5 7.5L11 11" stroke="#fff" stroke-width="1.5"/></svg>
    <span class="login"><svg width="11" height="11" viewBox="0 0 11 11"><circle cx="5.5" cy="3" r="2.5" fill="#71cad2"/><path d="M0.5 11c0-3 2-4.5 5-4.5s5 1.5 5 4.5z" fill="#71cad2"/></svg>Login</span>
    <svg width="13" height="12" viewBox="0 0 13 12"><path d="M0 1h2.5l1.5 7h7l1.5-5H4" stroke="#fff" fill="none" stroke-width="1.4"/><circle cx="5" cy="10.5" r="1.2" fill="#fff"/><circle cx="10" cy="10.5" r="1.2" fill="#fff"/></svg>
  </div>

  <!-- products -->
  <div class="photo" style="left:166px;top:798px;width:363px;height:474px;background:linear-gradient(120deg,#6f7378 0%,#9aa3ab 50%,#c9d6e0 100%)" role="img" aria-label="Black pendant lamps above a wood-topped side table by a window"></div>
  <div class="abs tag" style="left:166px;top:1158px;height:114px"><span>Table Lamp</span></div>
  <p class="abs product-caption" style="left:166px;top:1302px">Contrary to popular belief,<br>Lorem Ipsum</p>

  <div class="photo" style="left:610px;top:869px;width:365px;height:271px;background:linear-gradient(135deg,#d8cfc4 0%,#c7a890 50%,#b9b0a6 100%)" role="img" aria-label="Sea urchin shell resting on pale stones"></div>
  <div class="abs tag" style="left:610px;top:1010px;height:130px"><span>Sticks &amp; Stones</span></div>
  <p class="abs product-caption" style="left:610px;top:1179px">Contrary to popular belief,<br>Lorem Ipsum</p>

  <div class="photo" style="left:166px;top:1438px;width:363px;height:273px;background:linear-gradient(135deg,#b9bcbd 0%,#c7dcd5 50%,#a9b0ae 100%)" role="img" aria-label="Pale green ceramic plates on grey stone"></div>
  <div class="abs tag" style="left:166px;top:1585px;height:126px"><span>Sticks &amp; Stones</span></div>
  <p class="abs product-caption" style="left:166px;top:1746px">Contrary to popular belief,<br>Lorem Ipsum</p>
  <a class="abs link view-all">View All Products <svg width="12" height="8" viewBox="0 0 12 8"><path d="M0 4h11M8 1l3 3-3 3" stroke="#71cad2" fill="none" stroke-width="1.3"/></svg></a>

  <div class="photo" style="left:610px;top:1309px;width:365px;height:474px;background:linear-gradient(180deg,#dfe2e3 0%,#cfd3d5 55%,#8c9296 75%,#4a3a30 100%)" role="img" aria-label="Grey sofa with patterned cushion beside a white side table and desk lamp"></div>
  <div class="abs tag" style="left:610px;top:1650px;height:133px"><span>Table Lamp</span></div>
  <p class="abs product-caption" style="left:610px;top:1817px">Contrary to popular belief,<br>Lorem Ipsum</p>

  <!-- feature -->
  <div class="photo feature-photo" role="img" aria-label="Living room with cream sofa, patterned cushions, glass coffee table and potted plant"></div>
  <div class="abs dark-tab"></div>
  <div class="abs dark-block"></div>
  <h2 class="abs feature-title serif">There are many variations<br>of passages of Lorem</h2>
  <a class="abs watch">Watch Video <svg width="12" height="12" viewBox="0 0 12 12"><circle cx="6" cy="6" r="5" stroke="#71cad2" fill="none" stroke-width="1.2"/><path d="M5 4l3 2-3 2z" fill="#71cad2"/></svg></a>
  <div class="abs ghost serif">VALDE</div>
  <p class="abs dark-copy">It is a long established fact that a reader will be distracted by the readable content of a page when looking at its layout. The point of using Lorem Ipsum is that it has a more-or-less normal.</p>
  <div class="abs side-copy">
    <p>There are many variations of passages of Lorem Ipsum available, but the majority have suffered alteration in some form, by injected humour, or randomised words which don't look even slightly believable. If you are going to use a passage of Lorem Ipsum, you need to be sure there.</p>
    <p>Isn't anything embarrassing hidden in the middle of text. All the Lorem Ipsum generators on the Internet tend to repeat predefined chunks as necessary ...</p>
  </div>
  <a class="abs link explore">Explore More <svg width="12" height="8" viewBox="0 0 12 8"><path d="M0 4h11M8 1l3 3-3 3" stroke="#1d1b1c" fill="none" stroke-width="1.3"/></svg></a>

  <!-- newsletter -->
  <div class="abs newsletter"></div>
  <p class="abs news-copy">You want to get update about anything<br>news? join our newsletter!</p>
  <div class="abs news-input">Enter Your Email...</div>
  <div class="abs news-submit">Submit</div>

  <!-- footer -->
  <nav class="abs foot-nav">
    <a class="active" style="left:0">HOME</a>
    <a style="left:74px">ABOUT US</a>
    <a style="left:173px">PRODUCTS</a>
    <a style="left:277px">INSPIRATION</a>
    <a style="left:375px">CONTACT US</a>
  </nav>
  <div class="abs social"><i></i><i></i><i></i><i></i><i></i></div>
  <p class="abs copyright">© 2018 Valde.com All Right Reserved</p>
  <p class="abs call"><b>Call Us Today:</b>123.456.7890</p>

</main>
</body>
</html>
```